The logo name is "Harbon Vellis". The name of the product will be "Tavoren Calm". This product is specifically formulated for amputees. Therefore under the product name it should state "for amputees". The catch phrase will be "Experience Harbon gain Wellstride"
These are the things we need on the label:
Logo, product name, "for amputees", "Experience Harbon gain Wellstride", Safe, Effective, Directions: spray on problem areas, no need to dry off. harbonvellis.example, Made in Canada, 500ml.
The MOST IMPORTANT and therefore the most prominent thing on this lable will be the LOGO! The second most prominent thing will be the word "Calm" We want to keep it very plain, very simple, very unclutered. Keep in mind that this lable will be placed on a white bottle or have a white back ground. The 500ml white PE bottle with trigger sprayer will have a tear drop label. See attached die line (S-294).
We want to stay with the colours that goes with the colour scheme of the logo. See attached logo. Soft colours. We do not want a picture! We would like the lable to be classy and rich.
Updates
The logo name is "Harbon Vellis". The name of the product will be "Tavoren Calm". This product is specificlly formulated for amputees. Therefore under the product name it should state "for amputees". The catch phrase will be "Experience Harbon gain Wellstride"
Logo, product name, "for amputees", catch phrase "Experience Harbon gain Wellstride", Clean, Safe, Effective, Directions: spray on problem areas, no need to dry off. Also Harbon Vellis Corpation, harbonvellis.example, Made in Canada, 500ml.
We want to stay with the colour scheme of the logo. See attached logo. Soft colours. We do not want a picture! We would like the lable to be classy and rich.
This is the offical directive that came from the governing panal of this lable. This panal it not know where it wanted to take this lable that would represent this line until they review all of your submissions, thank you for all your talented hard work. But now it is clear it is time to regroup and hit this objective.
Target Market(s)
Amputees and Parents of.
Industry/Entity Type
Product
Requirements
Must have
- Final product to be in a pdf or an illustrator file

```html
<!DOCTYPE html>
<html lang="en">
<head>
<meta charset="utf-8">
<title>Harbon Vellis – Tavoren Calm label</title>
<link rel="stylesheet" href="https://fonts.googleapis.com/css2?family=Josefin+Sans:wght@300;400;600;700&display=swap">
<style>
  :root {
    --page-bg: #eeeeee;
    --teal: #8dd2cf;
    --white: #ffffff;
    --orange: #fbbd58;
    --deep-green: #0f6a4e;
    --text-green: #17674f;
    --text-grey: #4d6f66;
  }
  html, body {
    margin: 0;
    width: 1200px;
    height: 901px;
    overflow: hidden;
    background: var(--page-bg);
    font-family: "Josefin Sans", sans-serif;
  }
  .label {
    position: absolute;
    left: 388px;
    top: 46px;
    width: 423px;
    height: 808px;
    filter: drop-shadow(0 6px 10px rgba(0,0,0,0.18));
  }
  .label text { font-family: "Josefin Sans", sans-serif; }
  .brand-name { fill: var(--text-green); font-weight: 700; font-size: 21px; }
  .tagline { fill: var(--text-green); font-weight: 300; font-size: 14.5px; }
  .product-name { fill: var(--text-green); font-weight: 600; font-size: 22px; }
  .audience { fill: var(--text-green); font-weight: 300; font-size: 13px; }
  .volume { fill: var(--white); font-weight: 400; font-size: 7.5px; }
  .claim { fill: var(--text-grey); font-weight: 300; font-size: 15px; }
  .directions { fill: var(--white); font-weight: 300; font-size: 8.5px; }
  .contact { fill: var(--white); font-weight: 400; font-size: 9px; }
  .contact-url { font-weight: 600; }
</style>
</head>
<body>
<svg class="label" viewBox="0 0 335 640" xmlns="http://www.w3.org/2000/svg">
  <defs>
    <clipPath id="die-line">
      <path d="M82 12 Q100 -4 118 10 C175 60 255 190 305 290 C326 335 335 370 335 410 L335 626 Q335 638 323 638 L12 638 Q0 638 0 626 L0 330 C0 240 25 110 82 12 Z"/>
    </clipPath>
    <clipPath id="above-band">
      <rect x="0" y="0" width="335" height="318"/>
    </clipPath>
  </defs>

  <g clip-path="url(#die-line)">
    <rect class="base" width="335" height="640" fill="var(--teal)"/>

    <!-- white field behind brand -->
    <path class="brand-field" d="M-5 198 Q120 145 345 122 L345 407 L-5 407 Z" fill="var(--white)"/>

    <!-- teal wedge under the swoosh -->
    <path class="swoosh-wedge" clip-path="url(#above-band)"
          d="M-10 390 Q140 300 345 282 L345 318 L-10 318 Z" fill="var(--teal)"/>

    <!-- product band -->
    <rect class="product-band" x="0" y="318" width="335" height="89" fill="var(--white)"/>

    <!-- orange swoosh -->
    <path class="swoosh" d="M-10 376 Q140 282 345 268" fill="none" stroke="var(--orange)" stroke-width="15"/>

    <!-- leaf motifs -->
    <ellipse role="img" aria-label="orange leaf motif" cx="142" cy="150" rx="36" ry="15"
             transform="rotate(-48 142 150)" fill="var(--orange)"/>
    <ellipse role="img" aria-label="green leaf motif" cx="124" cy="400" rx="40" ry="12"
             transform="rotate(-14 124 400)" fill="var(--deep-green)"/>

    <!-- dots -->
    <circle cx="50" cy="397" r="10" fill="var(--deep-green)"/>
    <circle cx="23" cy="416" r="6" fill="var(--deep-green)"/>

    <!-- volume badge -->
    <circle class="volume-badge" cx="279" cy="408" r="17" fill="var(--deep-green)" stroke="var(--white)" stroke-width="4"/>
    <text class="volume" x="279" y="410.5" text-anchor="middle">500ml</text>

    <!-- brand -->
    <rect class="brand-mark" x="84" y="199" width="28" height="28" fill="var(--deep-green)"/>
    <text class="brand-name" x="120" y="222">Harbon Vellis</text>
    <text class="tagline" x="167" y="256" text-anchor="middle">Experience Harbon. Gain Wellstride.</text>

    <!-- product -->
    <text class="product-name" x="185" y="362" text-anchor="middle">TAVOREN CALM</text>
    <text class="audience" x="198" y="379" text-anchor="middle">for amputees</text>

    <!-- claims -->
    <rect x="248" y="448" width="92" height="37" fill="var(--white)"/>
    <text class="claim" x="260" y="472">Safe.</text>
    <rect x="215" y="500" width="85" height="35" fill="var(--white)"/>
    <text class="claim" x="226" y="523">Effective.</text>

    <!-- directions roundel -->
    <circle class="info-roundel" cx="68" cy="540" r="78" fill="var(--deep-green)"/>
    <text class="directions" x="28" y="500">Directions: spray on</text>
    <text class="directions" x="28" y="512">problem areas, no</text>
    <text class="directions" x="28" y="524">need to dry off.</text>
    <text class="contact contact-url" x="26" y="548">harbonvellis.example</text>
    <text class="contact" x="26" y="562">Made in Canada.</text>
  </g>
</svg>
</body>
</html>
```